Webdesign für Brandt Maler
Zielgruppe
Maler- und Bodenlegerarbeiten, Farbenherstellung, Fachmarkt
ZieIgruppe sind alle, die Fraben und/oder die Dienstleistungen der Firma benötigen
Aufgabenstellung
dem Kunde gefällt die Seite http://www.maler-quirinus.example/
bitte alle Uploads beachten
eigene Bilder und Stockmaterial

```html
<!DOCTYPE html>
<html lang="de">
<head>
<meta charset="utf-8">
<title>Brandt Maler – Wir renovieren komplett</title>
<link href="https://fonts.googleapis.com/css2?family=Lato:wght@300;400;700;900&display=swap" rel="stylesheet">
<style>
:root{
  --navy:#32359a;
  --red:#e8231f;
  --red-band:#ec2024;
  --text:#55565e;
  --white:#ffffff;
  --lavender:#d6d7ee;
  --rose:#f8cfd1;
}
*{box-sizing:border-box;margin:0;padding:0}
html,body{width:1200px;height:2325px;overflow:hidden;background:var(--white)}
body{position:relative;font-family:'Lato',sans-serif;color:var(--navy)}
.abs{position:absolute}
.center{left:0;width:1200px;text-align:center}

.brand{top:16px;left:0;width:1200px;display:flex;justify-content:center;align-items:center;gap:8px}
.brand-name{font-weight:900;font-size:30px;color:var(--navy);letter-spacing:.5px}
.brand-dot{width:14px;height:14px;border-radius:50%;background:var(--navy)}
.nav{top:70px;display:flex;justify-content:center;gap:28px;font-size:13px;font-weight:700;letter-spacing:.2px}
.nav a{color:var(--navy);text-decoration:none}
.nav a.active{color:var(--red)}

.splash{top:0;left:820px;width:380px;height:515px;
  background:radial-gradient(ellipse at 70% 20%,rgba(255,200,0,.75),transparent 45%),
             radial-gradient(ellipse at 40% 30%,rgba(30,120,220,.7),transparent 45%),
             radial-gradient(ellipse at 55% 55%,rgba(120,200,30,.6),transparent 45%),
             radial-gradient(ellipse at 85% 70%,rgba(240,120,40,.55),transparent 45%),
             radial-gradient(ellipse at 90% 10%,rgba(230,40,120,.6),transparent 35%);
  border-radius:0 0 0 60%}
.haze{top:0;left:0;width:400px;height:650px;
  background:radial-gradient(ellipse at 0% 20%,rgba(120,170,230,.45),transparent 55%),
             radial-gradient(ellipse at 0% 60%,rgba(240,150,120,.4),transparent 55%),
             radial-gradient(ellipse at 20% 40%,rgba(240,210,120,.35),transparent 50%)}

.hero-title{top:258px;font-size:63px;font-weight:300;line-height:1.1;color:var(--navy)}
.hero-title strong{font-weight:900}
.hero-lead{top:334px;font-size:13.5px;line-height:22px}
.hero-btn{top:398px;left:517px;width:166px;height:36px;border:2px solid var(--red);border-radius:18px;
  color:var(--red);font-size:14px;font-weight:700;display:flex;align-items:center;justify-content:center}

.band{top:527px;left:0;width:760px;height:369px}
.band-text{top:651px;left:150px;width:430px;text-align:center;color:var(--white);font-weight:900;font-size:28px;line-height:34px}
.roller{top:686px;left:36px;width:126px;height:206px;background:linear-gradient(160deg,#e82a2a 0%,#c81d1d 45%,#d9d9d9 60%,#b71d1d 100%);border-radius:40px 40px 10px 10px;opacity:.9}
.tile-panel{top:555px;left:602px;width:435px;height:311px;background:var(--white);border-radius:8px}
.tile{width:197px;height:140px;border-radius:8px}
.t1{top:564px;left:611px;background:linear-gradient(135deg,#b9a58a,#e9e6e0 60%,#8a6a4c)}
.t2{top:564px;left:830px;background:linear-gradient(180deg,#dedfe0,#c8cc5a 30%,#e4d6d2 70%,#d7c0c3)}
.t3{top:717px;left:611px;background:linear-gradient(135deg,#b3a7c4,#c9bfd4 55%,#7a5638)}
.t4{top:717px;left:830px;background:linear-gradient(90deg,#1d5c4c 0 30%,#dcdcdc 30%,#cfcac3 80%,#a2704f)}

.h2{font-weight:900;font-size:43px;line-height:1.1}
.welcome-title{top:963px}
.welcome-sub{top:1019px;font-size:13.5px}
.deco-lav{top:1017px;left:120px;width:112px;height:112px;border-radius:50%;background:var(--lavender)}
.deco-rose{top:1336px;left:1144px;width:112px;height:112px;border-radius:50%;background:var(--rose)}
.house{top:1072px;left:0;width:519px;height:350px;background:linear-gradient(180deg,#cfe0ee 0%,#f0e6c8 35%,#e9b658 55%,#f4f1ea 70%,#8a8c86 100%)}
.welcome-copy{top:1108px;left:565px;width:470px;font-size:13.5px;line-height:22.5px;color:var(--text)}

.gallery-title{top:1480px}
.gallery-sub{top:1539px;font-size:13.5px;line-height:22px;color:var(--text)}
.gallery{top:1602px;left:172px;width:854px;height:283px;display:grid;grid-template-columns:repeat(4,1fr);grid-template-rows:repeat(2,1fr);gap:1px}
.gallery div{width:100%;height:100%}
.g1{background:linear-gradient(135deg,#e5e7ea,#93b24a 60%,#36507e)}
.g2{background:linear-gradient(180deg,#b08a4a,#d8b57a 50%,#6c4a2a)}
.g3{background:linear-gradient(135deg,#e3e3e6,#dccb48 55%,#7b7f88)}
.g4{background:linear-gradient(180deg,#5d8fd0,#8a5a36 55%,#4d7a2a)}
.g5{background:linear-gradient(180deg,#3a78cf,#b8844f 55%,#7a6f66)}
.g6{background:linear-gradient(135deg,#b2261e,#c03a2a 45%,#6e7f88)}
.g7{background:linear-gradient(180deg,#f1f1f1,#c9a66a 60%,#d9d9d9)}
.g8{background:linear-gradient(180deg,#6b97d8,#b79c4c 55%,#3f5a27)}

.jobs-title{top:1977px}
.jobs-sub{top:2031px;font-size:13.5px;color:var(--text)}
.partners{top:2090px;left:172px;width:856px;display:flex;justify-content:space-between;align-items:center;height:34px}
.partner{font-weight:900;font-size:16px;color:var(--navy);letter-spacing:.3px}

.footer-wave{top:2180px;left:0;width:1200px;height:145px}
.footer-links{top:2237px;display:flex;justify-content:center;gap:20px;font-size:13.5px;color:var(--white)}
.footer-rule{top:2268px;left:350px;width:500px;height:1px;background:rgba(255,255,255,.35)}
.copyright{top:2285px;font-size:11.5px;color:var(--white)}
</style>
</head>
<body>

<div class="abs haze" role="img" aria-label="Weiche Farbnebel in Blau, Gelb und Rosa"></div>
<div class="abs splash" role="img" aria-label="Farbspritzer in Blau, Grün, Gelb, Orange und Pink"></div>

<header>
  <div class="abs brand"><span class="brand-name">BRANDT Maler</span><span class="brand-dot"></span></div>
  <nav class="abs center nav">
    <a class="active" href="#">HOME</a>
    <a href="#">LEISTUNGEN</a>
    <a href="#">AKTUELLE MELDUNGEN</a>
    <a href="#">UNTERNEHMEN</a>
    <a href="#">REFERENZEN</a>
    <a href="#">KONTAKT</a>
  </nav>
</header>

<section class="hero">
  <h1 class="abs center hero-title">Wir <strong>renovieren</strong> komplett</h1>
  <p class="abs center hero-lead">Die Firma Brandt Maler wurde 1921 gegründet und ist ein seit mehreren<br>Generationen geführtes Familienunternehmen.</p>
  <a class="abs hero-btn">+ Erfahren Sie mehr</a>
</section>

<section class="services">
  <svg class="abs band" viewBox="0 0 760 369" aria-hidden="true">
    <polygon points="192,0 750,0 622,369 70,369" fill="var(--red-band)"/>
    <polygon points="192,0 70,369 40,369 120,170" fill="var(--red-band)"/>
  </svg>
  <div class="abs roller" role="img" aria-label="Rote Farbrolle"></div>
  <p class="abs band-text">Maler - und Bodenlegerarbeiten<br>- Farbenherstellung - Fachmarkt</p>
  <div class="abs tile-panel"></div>
  <div class="abs tile t1" role="img" aria-label="Wohnraum mit Treppe und Sofa"></div>
  <div class="abs tile t2" role="img" aria-label="Wand mit Farbstreifen und Vase"></div>
  <div class="abs tile t3" role="img" aria-label="Lila Wand mit Esstisch"></div>
  <div class="abs tile t4" role="img" aria-label="Grün-weiße Wand mit Sessel"></div>
</section>

<section class="welcome">
  <div class="abs deco-lav"></div>
  <h2 class="abs center h2 welcome-title">Herzlich Willkommen</h2>
  <p class="abs center welcome-sub">Vielen Dank für Ihren Besuch auf unseren Internetseiten</p>
  <div class="abs house" role="img" aria-label="Firmengebäude mit bunten Fassaden"></div>
  <p class="abs welcome-copy">Wir freuen uns, dass Sie sich für unsere Firma interessieren und laden Sie recht herzlich ein, unser Unternehmen, unsere Serviceleistungen und unsere Produkte näher kennen zu lernen.<br>Unser Firmensitz befindet sich mitten im Herzen von Auental zwischen Lindenau, Hollbach und Kressenfeld, in der Flussstadt Birkental.<br>Unser höchstes Gebot ist es, stets für vollste Zufriedenheit unserer Kunden zu sorgen.<br>Auf den nachfolgenden Seiten haben wir für Sie allgemeine und fachspezifische Informationen rund um unsere Firma zusammengestellt. Verschaffen Sie sich einen Eindruck von der enormen Leistungsfähigkeit unseres Fachbetriebs, von der Kompetenz unserer Mitarbeiter und von den zahlreichen anderen Dingen, welche für unsere Kunden und Auftraggeber von großer Bedeutung sind.</p>
  <div class="abs deco-rose"></div>
</section>

<section class="gallery-section">
  <h2 class="abs center h2 gallery-title">Galerie</h2>
  <p class="abs center gallery-sub">Zahlreiche Unternehmen, Betriebe oder Privatpersonen zählen seit Jahren zu unseren Stammkunden.<br>Eine Vielzahl von Projekten konnten dabei verwirklicht und umgesetzt werden.</p>
  <div class="abs gallery">
    <div class="g1" role="img" aria-label="Aufenthaltsraum mit grüner Wand"></div>
    <div class="g2" role="img" aria-label="Festsaal mit Holzdecke"></div>
    <div class="g3" role="img" aria-label="Treppenhaus mit gelber Wand"></div>
    <div class="g4" role="img" aria-label="Holzhaus mit Garten"></div>
    <div class="g5" role="img" aria-label="Historisches Rathaus"></div>
    <div class="g6" role="img" aria-label="Halle mit roter Wand"></div>
    <div class="g7" role="img" aria-label="Heller Flur mit Holztüren"></div>
    <div class="g8" role="img" aria-label="Gelbes Wohnhaus"></div>
  </div>
</section>

<section class="jobs">
  <h2 class="abs center h2 jobs-title">JOBS - Angebote</h2>
  <p class="abs center jobs-sub">Wir arbeiten unter anderem mit</p>
  <div class="abs partners">
    <span class="partner">Wendel</span>
    <span class="partner">Farbwerk</span>
    <span class="partner">Colorano</span>
    <span class="partner">Nullpunkt</span>
    <span class="partner">Mineralis</span>
    <span class="partner">Bodena</span>
    <span class="partner">Fassado</span>
    <span class="partner">Krokolit</span>
  </div>
</section>

<footer>
  <svg class="abs footer-wave" viewBox="0 0 1200 145" preserveAspectRatio="none" aria-hidden="true">
    <path d="M0,40 C200,30 400,32 600,26 C800,20 950,14 1050,6 L1200,2 L1200,145 L0,145 Z" fill="var(--navy)"/>
    <path d="M900,18 L1045,0 L1040,6 L920,22 Z" fill="var(--navy)"/>
  </svg>
  <nav class="abs center footer-links"><span>Impressum</span><span>Kontakt</span><span>Datenschutz</span></nav>
  <div class="abs footer-rule"></div>
  <p class="abs center copyright">Copyright Netzwerk Webservice</p>
</footer>

</body>
</html>
```